looking to have a web site for the company which provides services in the industrial and commercial sectors such as: electrical, automation control and system integration, construction and maintenance, millwright, equipment assembly repair and installation. I have the domain already brivanholdings.net and logo. Most recent projects fulfilled for the following clients: MarlowKibbleCo, Dunholt University, OKSU, FALSTO, Tazzik, Prairie Grains

Target Market(s)

industrial and commercial sectors in electrical, automation, millwright and fabrication fields

Industry/Entity Type

Industrial

Coding

Coded - Design and coding required

Number of Pages Required

5+ page

Font styles to use
Sans Serif

Colors

Designer to choose colors to be used in the design.

Requirements
Nice to have
• looking to get something not complicated, nicely presented with minimum or no scrolling

```html
<!DOCTYPE html>
<html lang="en">
<head>
<meta charset="utf-8">
<title>Brivan Holdings Ltd – Our Processes</title>
<link rel="stylesheet" href="https://fonts.googleapis.com/css2?family=Rubik:wght@300;400;500;700&display=swap">
<style>
  :root {
    --navy: #093a4a;
    --white: #ffffff;
    --accent: #1a98cf;
    --heading: #2e2e2e;
    --muted: #8a8a8a;
    --page: #ffffff;
    --fab: #c9c9c9;
  }
  * { box-sizing: border-box; margin: 0; padding: 0; }
  html, body { width: 1200px; height: 675px; overflow: hidden; background: var(--page); }
  body { font-family: "Rubik", Arial, sans-serif; position: relative; }

  .site-header {
    position: absolute; top: 0; left: 0; width: 1200px; height: 66px;
    background: var(--navy); z-index: 2;
    display: flex; align-items: center;
  }
  .brand { position: absolute; left: 71px; top: 12px; display: flex; align-items: center; }
  .brand-badge {
    width: 148px; height: 42px; background: var(--white);
    display: flex; align-items: center; justify-content: center; gap: 7px;
    color: var(--navy); font-weight: 700; font-size: 13px; letter-spacing: 0.5px;
  }
  .brand-badge .mark { width: 12px; height: 12px; background: var(--navy); }
  .brand-name { margin-left: 8px; color: var(--white); font-weight: 700; font-size: 14.5px; letter-spacing: 0.2px; }

  .main-nav {
    position: absolute; left: 485px; top: 0; height: 66px;
    display: flex; align-items: center;
  }
  .nav-home { width: 24px; height: 24px; margin-right: 11px; }
  .nav-link {
    color: var(--white); font-weight: 500; font-size: 15px; margin-right: 19px;
    display: flex; align-items: center; gap: 5px; white-space: nowrap;
  }
  .caret { width: 0; height: 0; border-left: 4.5px solid transparent; border-right: 4.5px solid transparent; border-top: 5px solid var(--white); }
  .talk-button {
    position: absolute; left: 964px; top: 13px; width: 152px; height: 41px;
    background: var(--accent); border-radius: 21px; color: var(--white);
    font-weight: 500; font-size: 15.5px; display: flex; align-items: center; justify-content: center; gap: 9px;
  }
  .talk-button .dot { width: 22px; height: 22px; border: 2px solid var(--white); border-radius: 50%; }

  .section-title {
    position: absolute; top: 66px; left: 0; width: 1200px; text-align: center;
    font-weight: 300; font-size: 60px; color: var(--heading); line-height: 1;
  }
  .section-subtitle {
    position: absolute; top: 158px; left: 0; width: 1200px; text-align: center;
    font-weight: 300; font-size: 20px; color: var(--muted);
  }

  .timeline-line { position: absolute; left: 599px; top: 256px; width: 2px; height: 420px; background: var(--navy); }
  .timeline-dot { position: absolute; left: 591px; width: 18px; height: 18px; border-radius: 50%; background: var(--navy); }

  .process-card {
    position: absolute; width: 438px; background: var(--navy); color: var(--white);
  }
  .card-left { left: 120px; top: 222px; height: 206px; padding: 28px 36px 0 40px; text-align: right; }
  .card-right { left: 642px; top: 475px; height: 220px; padding: 52px 40px 0 36px; text-align: left; }
  .card-title { font-weight: 500; font-size: 22px; margin-bottom: 18px; }
  .card-text { font-weight: 400; font-size: 14.5px; line-height: 21.5px; }

  .back-to-top {
    position: absolute; left: 1040px; top: 584px; width: 53px; height: 53px;
    border-radius: 50%; background: var(--fab); display: flex; align-items: center; justify-content: center;
  }
</style>
</head>
<body>
  <header class="site-header">
    <div class="brand">
      <div class="brand-badge"><span class="mark"></span>BRIVAN</div>
      <span class="brand-name">BRIVAN HOLDINGS LTD</span>
    </div>
    <nav class="main-nav">
      <svg class="nav-home" viewBox="0 0 24 24" fill="none" stroke="#ffffff" stroke-width="1.6">
        <path d="M2 12 L12 3 L22 12"/><path d="M5 10 V21 H10 V15 H14 V21 H19 V10"/>
      </svg>
      <span class="nav-link">About Us <span class="caret"></span></span>
      <span class="nav-link">Services <span class="caret"></span></span>
      <span class="nav-link">Investors</span>
      <span class="nav-link">Our Work <span class="caret"></span></span>
      <span class="nav-link">Careers</span>
    </nav>
    <div class="talk-button"><span class="dot"></span>Talk to Us</div>
  </header>

  <h1 class="section-title">Our Processes</h1>
  <p class="section-subtitle">We make your vision become a reality</p>

  <div class="timeline-line"></div>
  <div class="timeline-dot" style="top:247px"></div>
  <div class="timeline-dot" style="top:497px"></div>

  <article class="process-card card-left">
    <h2 class="card-title">Sure choice</h2>
    <p class="card-text">An active feedback loop ensures all opportunities for improvement are captured in our master templates to assure your project goes from design to implementation in the shortest time and at the lowest cost possible.</p>
  </article>

  <article class="process-card card-right">
    <p class="card-text">Your day shouldn't be filled managing the consultants while also co-coordinating their work. Our proactive nature means we present these opportunities to you.</p>
  </article>

  <div class="back-to-top">
    <svg width="28" height="30" viewBox="0 0 28 30" fill="none" stroke="#ffffff" stroke-width="2">
      <path d="M14 29 V2"/><path d="M2 14 L14 2 L26 14"/>
    </svg>
  </div>
</body>
</html>
```